K7T Business Cards

I need a very sleek design using the logo attached. I want something very simple and clean, yet still creative. On the black I would like some sort of matte black finish, so make the design that will fit that accordingly.

I have attached the information needed in the card with the logo image.

Business

```html
<!DOCTYPE html>
<html lang="en">
<head>
<meta charset="utf-8">
<title>K7T Business Cards</title>
<link href="https://fonts.googleapis.com/css2?family=Arimo&family=Open+Sans:wght@600;800&display=swap" rel="stylesheet">
<style>
  :root {
    --page: #ebe8e3;
    --card-light: #ffffff;
    --card-dark: #121417;
    --card-dark-edge: #050607;
    --brand-blue: #1a5fb4;
    --accent-red: #e8262b;
    --accent-orange: #f7931e;
    --accent-yellow: #ffc20e;
    --text-light: #f2f2f2;
    --rule: #b9bcc0;
  }
  html, body {
    margin: 0;
    width: 1200px;
    height: 899px;
    overflow: hidden;
    background: var(--page);
  }
  .canvas { position: relative; width: 1200px; height: 899px; }
  .card {
    position: absolute;
    width: 637px;
    height: 363px;
    border-radius: 18px;
    overflow: hidden;
    box-shadow: 0 4px 10px rgba(0,0,0,0.25);
  }
  .card-front { left: 122px; top: 87px; background: var(--card-light); }
  .card-back {
    left: 464px; top: 471px;
    background: radial-gradient(ellipse at 50% 45%, #24272b 0%, var(--card-dark) 55%, var(--card-dark-edge) 100%);
  }
  .front-top { position: absolute; left: 0; top: 0; width: 100%; height: 184px; }
  .accent-stripe {
    position: absolute; left: 0; top: 184px; width: 100%; height: 4px;
    background: linear-gradient(90deg, var(--accent-red), var(--accent-orange) 60%, var(--accent-yellow));
  }
  .front-bottom {
    position: absolute; left: 0; top: 188px; width: 100%; height: 175px;
    background: radial-gradient(ellipse at 40% 30%, #25282c 0%, var(--card-dark) 60%, var(--card-dark-edge) 100%);
  }
  .brand-lockup { position: absolute; display: flex; align-items: center; height: 128px; }
  .brand-square { width: 62px; height: 62px; background: var(--brand-blue); }
  .brand-divider { width: 2px; height: 100%; background: var(--rule); margin: 0 18px 0 68px; }
  .brand-name {
    font-family: "Open Sans", sans-serif; font-weight: 800;
    color: var(--brand-blue); font-size: 28px; line-height: 1.05;
    letter-spacing: 1px; text-transform: uppercase;
  }
  .card-front .brand-lockup { left: 148px; top: 30px; }
  .card-back .brand-lockup { left: 144px; top: 120px; height: 110px; }
  .person { position: absolute; left: 40px; top: 58px; color: var(--text-light); font-family: "Arimo", sans-serif; }
  .person-name { font-size: 30px; line-height: 1; }
  .person-title { font-size: 19px; margin-top: 4px; }
  .contact-list {
    position: absolute; left: 444px; top: 17px; margin: 0; padding: 0; list-style: none;
    font-family: "Open Sans", sans-serif; font-weight: 600; font-size: 16px; color: var(--text-light);
  }
  .contact-list li { display: flex; align-items: center; height: 35px; }
  .contact-list svg { width: 22px; height: 22px; margin-right: 12px; flex: none; }
  .back-url {
    position: absolute; left: 0; width: 100%; top: 321px; text-align: center;
    font-family: "Open Sans", sans-serif; font-weight: 600; font-size: 16px; color: var(--text-light);
  }
</style>
</head>
<body>
<div class="canvas">
  <section class="card card-front">
    <div class="front-top"></div>
    <div class="brand-lockup">
      <div class="brand-square"></div>
      <div class="brand-divider"></div>
      <div class="brand-name">Harwick<br>Marketing</div>
    </div>
    <div class="accent-stripe"></div>
    <div class="front-bottom">
      <div class="person">
        <div class="person-name">Marcus Harwick</div>
        <div class="person-title">Sales Executive</div>
      </div>
      <ul class="contact-list">
        <li><svg viewBox="0 0 24 24" fill="none" stroke="#f2f2f2" stroke-width="1.6"><path d="M5 3l4 1 1 5-2 2c1 3 3 5 6 6l2-2 5 1 1 4-3 2C10 22 2 14 3 6z"/></svg>555.014.0219</li>
        <li><svg viewBox="0 0 24 24" fill="none" stroke="#f2f2f2" stroke-width="1.6"><rect x="6" y="2" width="12" height="20" rx="1.5"/><line x1="6" y1="17" x2="18" y2="17"/></svg>555.014.0219</li>
        <li><svg viewBox="0 0 24 24" fill="none" stroke="#f2f2f2" stroke-width="1.6"><rect x="2" y="5" width="20" height="14"/><path d="M2 5l10 8 10-8M2 19l7-7M22 19l-7-7"/></svg>marcus@k7t.net</li>
        <li><svg viewBox="0 0 24 24" fill="none" stroke="#f2f2f2" stroke-width="1.6"><circle cx="12" cy="12" r="9.5"/><ellipse cx="12" cy="12" rx="4.5" ry="9.5"/><line x1="2.5" y1="12" x2="21.5" y2="12"/><path d="M4 7h16M4 17h16"/></svg>www.k7t.net</li>
      </ul>
    </div>
  </section>

  <section class="card card-back">
    <div class="brand-lockup">
      <div class="brand-square"></div>
      <div class="brand-divider"></div>
      <div class="brand-name">Harwick<br>Marketing</div>
    </div>
    <div class="back-url">www.k7t.net</div>
  </section>
</div>
</body>
</html>
```